Postcard Design Project

We sells Laser Printer Ink and Toners, We also sells on Brindlo Market Place, Need a post card for these brindlo contact to start buying through our website instead of Brindlo. Company Name: Ky Office Wares LLC, website is www.kyprintvo.com phone#718-555-0142

```html
<!DOCTYPE html>
<html lang="en">
<head>
<meta charset="utf-8">
<title>Ky Office Wares Postcard</title>
<link rel="stylesheet" href="https://fonts.googleapis.com/css2?family=Oswald:wght@500;600&family=Lato:wght@400;700&display=swap">
<style>
  :root {
    --blue: #2a8fcb;
    --blue-light: #35aee2;
    --yellow: #f2d23a;
    --yellow-deep: #e8bf22;
    --magenta: #ea168f;
    --grey-band: #e6e6e6;
    --charcoal: #333333;
    --ink: #222222;
    --red: #e02222;
    --white: #ffffff;
  }
  * { margin: 0; padding: 0; box-sizing: border-box; }
  html, body { width: 1200px; height: 903px; overflow: hidden; background: #f2f2f2; }
  .postcard { position: relative; width: 1200px; height: 903px; background: var(--white); overflow: hidden; font-family: "Lato", sans-serif; }
  .shapes { position: absolute; inset: 0; }
  .text { position: absolute; white-space: nowrap; }
  .headline { left: 46px; top: 62px; font-family: "Oswald", sans-serif; font-weight: 600; font-size: 74px; color: var(--white); letter-spacing: 1px; }
  .offer-main { left: 46px; top: 222px; font-family: "Oswald", sans-serif; font-weight: 600; font-size: 72px; color: var(--ink); line-height: 1; }
  .offer-sub { left: 48px; top: 310px; font-family: "Oswald", sans-serif; font-weight: 500; font-size: 50px; color: var(--ink); line-height: 1; }
  .promo { left: 48px; top: 432px; font-weight: 700; font-size: 29px; color: var(--white); line-height: 1.25; }
  .call-label { left: 185px; top: 535px; font-size: 29px; color: var(--ink); }
  .phone { left: 118px; top: 572px; font-family: "Oswald", sans-serif; font-weight: 600; font-size: 68px; color: var(--red); line-height: 1.1; }
  .phone-icon { position: absolute; left: 50px; top: 592px; width: 52px; height: 52px; }
  .brand { left: 62px; top: 728px; display: flex; align-items: center; gap: 14px; font-weight: 700; font-size: 34px; color: var(--ink); }
  .brand-dot { width: 34px; height: 34px; border-radius: 50%; background: var(--magenta); }
  .visit-label { left: 460px; top: 770px; font-weight: 700; font-size: 29px; color: var(--ink); }
  .website { left: 200px; top: 840px; font-size: 40px; letter-spacing: 6px; color: var(--white); }
</style>
</head>
<body>
<main class="postcard">
  <svg class="shapes" width="1200" height="903" viewBox="0 0 1200 903">
    <defs>
      <linearGradient id="blueGrad" x1="0" y1="0" x2="1" y2="0">
        <stop offset="0" stop-color="var(--blue)"/>
        <stop offset="1" stop-color="var(--blue-light)"/>
      </linearGradient>
      <linearGradient id="yellowGrad" x1="0" y1="0" x2="1" y2="0">
        <stop offset="0" stop-color="var(--yellow-deep)"/>
        <stop offset="1" stop-color="var(--yellow)"/>
      </linearGradient>
      <linearGradient id="photoGrad" x1="0" y1="0" x2="1" y2="1">
        <stop offset="0" stop-color="#eceae6"/>
        <stop offset="0.55" stop-color="#cfd1d3"/>
        <stop offset="1" stop-color="#6c7580"/>
      </linearGradient>
      <clipPath id="cardClip"><rect width="1200" height="903"/></clipPath>
    </defs>
    <g clip-path="url(#cardClip)">
      <path class="band-blue" d="M0 0 H1200 V560 L900 200 H0 Z" fill="url(#blueGrad)"/>
      <rect class="band-yellow" x="0" y="200" width="900" height="220" fill="url(#yellowGrad)"/>
      <rect class="band-magenta" x="0" y="420" width="900" height="100" fill="var(--magenta)"/>
      <rect class="band-grey" x="0" y="520" width="900" height="160" fill="var(--grey-band)"/>
      <path class="corner-magenta" d="M1200 560 V903 H900 Z" fill="var(--magenta)"/>
      <path class="band-footer" d="M0 832 H780 C830 832 850 838 880 860 L930 903 H0 Z" fill="var(--charcoal)"/>
      <rect x="633" y="153" width="594" height="594" rx="46" transform="rotate(45 930 450)" fill="var(--white)" stroke="#1a1a1a" stroke-width="3"/>
      <rect role="img" aria-label="Photo of a smiling technician repairing an office laser printer" x="645" y="165" width="570" height="570" rx="38" transform="rotate(45 930 450)" fill="url(#photoGrad)"/>
    </g>
  </svg>

  <h1 class="text headline">GOT DIRTY PRINTER?</h1>
  <p class="text offer-main">GET A TECHNICIAN</p>
  <p class="text offer-sub">IN YOUR OFFICE TODAY</p>
  <p class="text promo">Also check out our unbeatable<br>Ink and toner online prices.</p>
  <p class="text call-label">Call Us Today</p>
  <svg class="phone-icon" viewBox="0 0 52 52" aria-hidden="true">
    <circle cx="26" cy="26" r="23" fill="none" stroke="var(--blue)" stroke-width="2.5"/>
    <path d="M18 15 l5 -2 l4 8 l-3 3 c1 4 4 7 8 8 l3 -3 l8 4 l-2 5 c-12 1 -24 -11 -23 -23 Z" fill="var(--blue)"/>
  </svg>
  <p class="text phone">718-555-0142</p>
  <div class="text brand"><span class="brand-dot"></span>Ky Office Wares</div>
  <p class="text visit-label">Visit Us online:</p>
  <p class="text website">www.kyprintvo.com</p>
</main>
</body>
</html>
```